依頼詳細
デザインを依頼する製品の名前は「雲居そば」です。
表面のデザイン作成をお願いします。

【デザインイメージ】
・シックで高級感のあるデザインが好ましいです。
・希望の色はベースが黒色で商品名の「雲居そば」は金色でお願いします。

【必須記載事項】
下記の文言は必ずデザイン上に記載をお願いします。
・ゆで時間4~5分
・内容量220g
・「謹製」(四角の判子風)
・「本場信州の伝統の味」
・「そばの豊かな香りと喉ごしの良さを楽しめます」

【その他製品特徴】
下記はその他製品の特徴になります。デザインへの記載は各ランサー様へお任せします。
・本品「雲居そば」は、本場信州の恵まれた気候風土と長年の経験の中から独自の製法を編み出し、生まれました。のどごしの良いなめらかな食感と風味豊かな香りを楽しめるそばに仕上げました。
・本品は贈答品で使用することが多いため、化粧箱に入っている状態で見栄えが良く見えるデザインをお願いします。また参考となる画像を添付いたします。
記載項目
製品サイズ(実寸):295×75(mm)
希望イメージ
シンプル 複雑
単色 カラフル
暗い 明るい
日常 高級
遊び心 厳粛
未来的 伝統的
女性的 男性的
希望する色
無彩色系
納品ファイル
• 高解像度JPG (.jpg)
• イラストレーター形式 (.ai)

当社がイメージした通り、シックで高級感があり化粧箱に入っている状態で見栄えが良く見えるデザインで、社内のアンケートでも好評だったため選定させていただきました。

この度は、たくさんのご提案を頂き、大変ありがとうございます。
さまざまなデザイン案やコンセプトがあり、選考に時間をいただいてしまいました。
提案者の皆様の非常にクオリティの高い提案に加え、さまざまな方向性のデザインがありとても良い勉強になりました。

```html
<!DOCTYPE html>
<html lang="ja">
<head>
<meta charset="utf-8">
<title>雲居そば パッケージ</title>
<link rel="stylesheet" href="https://fonts.googleapis.com/css2?family=Shippori+Mincho:wght@400;500&family=Shippori+Mincho+B1:wght@800&display=swap">
<style>
  :root{
    --ink:#2b272b;
    --band-dark:#1c191a;
    --band-tint:#3b3324;
    --gold:#b39a3f;
    --gold-soft:#8f7a34;
    --seal-red:#b8454a;
    --paper:#f4f1ea;
  }
  *{margin:0;padding:0;box-sizing:border-box}
  html,body{width:1200px;height:4456px;overflow:hidden;background:var(--ink)}
  .package{position:relative;width:1200px;height:4456px;background:var(--ink);font-family:"Shippori Mincho",serif}
  .pattern-band{position:absolute;left:0;width:1200px;background:linear-gradient(135deg,var(--band-dark),var(--band-tint) 50%,var(--band-dark))}
  .pattern-band--top{top:0;height:740px}
  .pattern-band--bottom{top:4160px;height:296px}
  .frame{position:absolute;left:0;top:0}
  .product-name{position:absolute;left:510px;top:1300px;writing-mode:vertical-rl;font-size:180px;font-weight:400;color:var(--gold);letter-spacing:8px;line-height:1}
  .sheaf{position:absolute;top:1580px;width:160px;height:420px;border-radius:80px;background:linear-gradient(180deg,var(--gold),var(--gold-soft))}
  .sheaf--left{left:250px}
  .sheaf--right{left:790px}
  .seal{position:absolute;left:558px;top:2100px;width:84px;height:172px;border:4px solid var(--seal-red);display:flex;align-items:center;justify-content:center}
  .seal span{writing-mode:vertical-rl;font-size:56px;color:var(--seal-red);line-height:1;letter-spacing:4px}
  .tagline{position:absolute;left:0;width:1200px;top:2268px;text-align:center;font-family:"Shippori Mincho B1",serif;font-weight:800;font-size:70px;color:var(--gold);letter-spacing:4px}
  .description{position:absolute;left:520px;top:2590px;writing-mode:vertical-rl;font-size:62px;color:var(--paper);line-height:104px;letter-spacing:12px}
  .boil-time{position:absolute;left:88px;top:3620px;width:312px;height:250px;border:4px solid var(--paper);border-radius:36px;color:var(--paper);text-align:center}
  .boil-time__label{display:block;font-size:38px;margin-top:26px}
  .boil-time__value{display:block;font-size:84px;margin-top:14px;letter-spacing:2px}
  .net-weight{position:absolute;left:88px;top:3920px;font-size:68px;color:var(--paper)}
</style>
</head>
<body>
<main class="package">
  <div class="pattern-band pattern-band--top" role="img" aria-label="金の麻の葉文様の帯"></div>

  <svg class="frame" width="1200" height="4456" viewBox="0 0 1200 4456" aria-hidden="true">
    <path d="M168 1060 H1032 V1088 H1060 V2392 H1032 V2420 H168 V2392 H140 V1088 H168 Z" fill="none" stroke="var(--gold)" stroke-width="4"/>
  </svg>

  <div class="sheaf sheaf--left" role="img" aria-label="金色の稲穂飾り（左）"></div>
  <div class="sheaf sheaf--right" role="img" aria-label="金色の稲穂飾り（右）"></div>

  <h1 class="product-name">雲居そば</h1>

  <div class="seal"><span>謹製</span></div>

  <p class="tagline">本場信州の伝統の味</p>

  <p class="description">そばの豊かな香りと<br>喉ごしの良さを楽しめます</p>

  <div class="boil-time">
    <span class="boil-time__label">ゆで時間</span>
    <span class="boil-time__value">4～5分</span>
  </div>
  <p class="net-weight">内容量 220g</p>

  <div class="pattern-band pattern-band--bottom" role="img" aria-label="金の麻の葉文様の帯"></div>
</main>
</body>
</html>
```